Customs House descriptive business cards

We require a two-sided business card that has a simple yet elegant design. We want to be able to promote our services as a customs house. This card should include our logo, contact info and services offered with the logo being on one side and the contact info and services on the flip side

Target Market(s)

Importers / exporters to and from the Bahamas

Industry/Entity Type

Logistics

Contact Information for Business Card

The front side of the card could have the logo and the flip side should have the other relevant info

Font styles to use
Serif

Colors

Designer to choose colors to be used in the design.

Requirements
Must have
• (Kelpway Brokers Ltd) Logo, address and contact info also services:
• import customs clearance, Delivery & HAndling services,Florida pickups, Export packing & Crating Services, export customs clearance, Consulting

```html
<!DOCTYPE html>
<html lang="en">
<head>
<meta charset="utf-8">
<title>Kelpway Brokers Ltd – Business Cards</title>
<link rel="stylesheet" href="https://fonts.googleapis.com/css2?family=Open+Sans:wght@400;600;700&display=swap">
<style>
  :root {
    --brand-blue: #2a7cc7;
    --brand-blue-dark: #1f68ad;
    --brand-blue-light: #4a97da;
    --band-grey: #b9bcc0;
    --text-grey: #555a60;
    --card-white: #ffffff;
    --canvas-bg: #e4e6e9;
  }
  * { box-sizing: border-box; margin: 0; padding: 0; }
  html, body {
    width: 1200px; height: 800px; overflow: hidden;
    background: var(--canvas-bg);
    font-family: "Open Sans", Arial, sans-serif;
  }
  .stage {
    position: relative; width: 1200px; height: 800px;
    display: flex; align-items: center; justify-content: center; gap: 50px;
  }
  .card {
    position: relative; width: 525px; height: 300px;
    overflow: hidden; box-shadow: 0 6px 18px rgba(0,0,0,0.15);
  }

  /* Contact side */
  .card--contact { background: var(--card-white); }
  .contact__edge {
    position: absolute; left: 0; top: 40px; bottom: 40px; width: 10px;
    background: var(--brand-blue);
  }
  .contact__details { position: absolute; left: 42px; top: 44px; color: var(--text-grey); }
  .contact__name { color: var(--brand-blue); font-weight: 700; font-size: 19px; }
  .contact__title { font-size: 13px; margin-bottom: 18px; }
  .contact__address { font-size: 12.5px; line-height: 1.45; margin-bottom: 8px; }
  .contact__line { display: flex; align-items: center; gap: 8px; font-size: 12.5px; line-height: 1.55; }
  .contact__line svg { width: 11px; height: 11px; flex: none; }
  .contact__brand {
    position: absolute; right: 40px; top: 125px;
    display: flex; align-items: center; gap: 10px;
    color: var(--brand-blue); font-weight: 600; font-size: 22px; letter-spacing: 0.5px;
  }
  .brand-mark { width: 14px; height: 14px; background: currentColor; flex: none; }
  .contact__web {
    position: absolute; right: 40px; bottom: 44px;
    color: var(--text-grey); font-size: 13px;
  }
  .contact__footbar {
    position: absolute; right: 0; bottom: 0; width: 300px; height: 12px;
    background: var(--brand-blue);
  }

  /* Brand side */
  .card--brand { background: var(--brand-blue); color: var(--card-white); }
  .brand__name {
    position: absolute; left: 0; right: 0; top: 78px;
    display: flex; justify-content: center; align-items: center; gap: 12px;
    font-weight: 600; font-size: 30px; letter-spacing: 1px;
  }
  .brand__name .brand-mark { width: 18px; height: 18px; }
  .brand__services {
    position: absolute; left: 28px; right: 28px; top: 172px;
    text-align: center; font-size: 12.5px; line-height: 1.6;
  }
  .brand__band {
    position: absolute; left: 0; right: 0; bottom: 46px; height: 14px;
    background: var(--band-grey);
  }
  .brand__foot {
    position: absolute; left: 0; right: 0; bottom: 0; height: 46px;
    background: var(--brand-blue-dark);
    display: flex; align-items: center; justify-content: center;
    font-size: 13px; letter-spacing: 0.3px;
  }
</style>
</head>
<body>
<main class="stage">

  <section class="card card--contact" aria-label="Business card, contact side">
    <div class="contact__edge"></div>
    <div class="contact__details">
      <p class="contact__name">Marcus Rolle</p>
      <p class="contact__title">Operations Director</p>
      <p class="contact__address">#42 Coral Ridge Road<br>P.O. Box SP-40217<br>Nassau, Bahamas</p>
      <p class="contact__line">
        <svg viewBox="0 0 12 12" aria-hidden="true"><path d="M2 1h2.5l1 3-1.5 1a7 7 0 0 0 3 3l1-1.5 3 1V10a1 1 0 0 1-1 1A9 9 0 0 1 1 2a1 1 0 0 1 1-1z" fill="var(--brand-blue)"/></svg>
        (242) 555-0143
      </p>
      <p class="contact__line">
        <svg viewBox="0 0 12 12" aria-hidden="true"><rect x="3" y="0.8" width="6" height="10.4" rx="1" fill="none" stroke="var(--brand-blue)" stroke-width="1.2"/><circle cx="6" cy="9.4" r="0.6" fill="var(--brand-blue)"/></svg>
        (242) 555-0178
      </p>
      <p class="contact__line">
        <svg viewBox="0 0 12 12" aria-hidden="true"><rect x="0.8" y="2.2" width="10.4" height="7.6" fill="none" stroke="var(--brand-blue)" stroke-width="1.2"/><path d="M1 2.5l5 4 5-4" fill="none" stroke="var(--brand-blue)" stroke-width="1.2"/></svg>
        imports@kelpwaybrokersltd.com
      </p>
    </div>
    <div class="contact__brand"><span class="brand-mark"></span>Kelpway Brokers Ltd</div>
    <p class="contact__web">www.kelpwaybrokersltd.com</p>
    <div class="contact__footbar"></div>
  </section>

  <section class="card card--brand" aria-label="Business card, brand side">
    <div class="brand__name"><span class="brand-mark"></span>Kelpway Brokers Ltd</div>
    <p class="brand__services">
      Import Customs Clearance | Delivery &amp; Handling Services | Florida Pickups<br>
      Export Packing &amp; Crating Services | Export Customs Clearance | Consulting
    </p>
    <div class="brand__band"></div>
    <div class="brand__foot">www.kelpwaybrokersltd.com</div>
  </section>

</main>
</body>
</html>
```